Financial Advisor Resource Firm needs business card design

Need business card design for company in Omaha NE called Tallowbrook Partners. We provide resources to financial advisors....workshop programs, retirement analysis, and insurance planning. I would like to see designs that use grays, greens, black, and white colors. The final design should communicate 'collaboration' and be simple yet attractive to financial planning clients. I will attached our logo and another picture of a puzzle piece coming together. I would like the incorporate the puzzle picture somehow, maybe on the back somehow, with color or just the gray scale....OR, the picture be the front of the card with 'Tallowbrook' definition on it (see upload) and then company logo, employee name, title, address on the back (see ppt uploaded). The following disclosure needs to be included somewhere- Advisory services offered through Marlowe Ridge Advisors, LLC.
Updates

I uploaded a svg and ai file of the logo

Target Market(s)

Financial planning clients and financial advisors....so pretty diverse age range of about 40-70.

Industry/Entity Type

Financial Planning

Contact Information for Business Card

Dennis K. Holloway, MBA
Founder/President
5727 E. Larkspur Avenue
Suite 418
Omaha, NE 68297
Phone- (402) 555-0147
Cell- (402) 555-0183
Fax- (402) 555-0129
email- dennis@tallowbrookgroup.example
web address- www.tallowbrookgroup.example

Colors
1b1b1b
474747
d3d3d3
ffffff
9bcb3c
abd036

Requirements
Must have
• Must include logo provided, must be 2 sided, and must have disclosure...all of these items listed in project description

```html
<!DOCTYPE html>
<html lang="en">
<head>
<meta charset="utf-8">
<title>Tallowbrook Partners – Business Card</title>
<link rel="stylesheet" href="https://fonts.googleapis.com/css2?family=Cinzel:wght@500;600&family=Arimo:wght@400;500&display=swap">
<style>
  :root {
    --ink: #1b1b1b;
    --graphite: #474747;
    --silver: #d3d3d3;
    --paper: #ffffff;
    --leaf: #9bcb3c;
    --lime: #abd036;
    --backdrop: #e9e9e6;
  }
  * { margin: 0; padding: 0; box-sizing: border-box; }
  html, body { width: 1200px; height: 780px; overflow: hidden; }
  body {
    background: var(--backdrop);
    position: relative;
    font-family: "Arimo", Arial, sans-serif;
    color: var(--graphite);
  }
  .card {
    position: absolute;
    top: 235px;
    width: 540px;
    height: 310px;
    border-radius: 14px;
    overflow: hidden;
    background: linear-gradient(160deg, #ffffff 0%, #f1f1f1 100%);
    box-shadow: 0 1px 0 var(--silver), 0 12px 30px rgba(0,0,0,0.18);
  }
  .card--front { left: 40px; }
  .card--back { left: 620px; }
  .card-art { position: absolute; inset: 0; width: 100%; height: 100%; }

  .brand {
    position: absolute;
    display: flex;
    align-items: center;
    gap: 12px;
  }
  .brand-dot {
    width: 22px; height: 22px;
    border-radius: 50%;
    background: var(--leaf);
    flex: none;
  }
  .brand-name {
    font-family: "Cinzel", Georgia, serif;
    font-weight: 600;
    color: var(--ink);
    letter-spacing: 0.02em;
    white-space: nowrap;
  }
  .card--front .brand { left: 36px; top: 46px; }
  .card--front .brand-name { font-size: 25px; }
  .card--back .brand { left: 50%; top: 50%; transform: translate(-50%, -50%); }
  .card--back .brand-name { font-size: 27px; }

  .contact {
    position: absolute;
    left: 36px;
    top: 112px;
    display: flex;
    font-size: 10.5px;
    line-height: 16px;
    color: var(--graphite);
  }
  .contact-col { padding: 0 14px; border-left: 1px solid var(--silver); }
  .contact-col:first-child { padding-left: 0; border-left: none; }
  .phone-line { display: flex; align-items: center; gap: 6px; }
  .phone-icon {
    width: 11px; height: 11px; border-radius: 50%;
    background: var(--leaf);
    display: inline-flex; align-items: center; justify-content: center;
  }
  .phone-icon svg { width: 7px; height: 7px; }
  .web-accent { color: var(--leaf); }

  .disclosure {
    position: absolute;
    left: 36px;
    top: 178px;
    font-size: 9px;
    line-height: 12px;
    color: var(--graphite);
    letter-spacing: 0.01em;
    white-space: nowrap;
  }

  .person {
    position: absolute;
    right: 26px;
    bottom: 22px;
    text-align: right;
  }
  .person-name {
    font-family: "Cinzel", Georgia, serif;
    font-weight: 500;
    font-size: 14px;
    color: var(--ink);
    letter-spacing: 0.02em;
  }
  .person-title {
    font-size: 11px;
    color: var(--paper);
    margin-top: 2px;
  }
</style>
</head>
<body>

<section class="card card--front" aria-label="Card front">
  <svg class="card-art" viewBox="0 0 540 310" preserveAspectRatio="none" aria-hidden="true">
    <defs>
      <linearGradient id="leafFront" x1="0" y1="0" x2="1" y2="1">
        <stop offset="0" stop-color="#abd036"/>
        <stop offset="1" stop-color="#8fbf34"/>
      </linearGradient>
    </defs>
    <path d="M0,246 C190,234 390,200 522,150 C430,196 220,262 0,284 Z" fill="#1b1b1b"/>
    <path d="M0,310 L0,290 C200,270 410,214 540,160 L540,310 Z" fill="url(#leafFront)"/>
  </svg>

  <div class="brand">
    <span class="brand-dot"></span>
    <span class="brand-name">Tallowbrook Partners</span>
  </div>

  <div class="contact">
    <div class="contact-col">
      <div class="phone-line"><span class="phone-icon"><svg viewBox="0 0 10 10"><path d="M2 1 L4 1 L4.6 3 L3.5 3.8 C4 5 5 6 6.2 6.5 L7 5.4 L9 6 L9 8 C5 8.5 1.5 5 2 1 Z" fill="#fff"/></svg></span>(402) 555-0147</div>
      <div class="phone-line"><span class="phone-icon"><svg viewBox="0 0 10 10"><rect x="3" y="1" width="4" height="8" rx="0.8" fill="#fff"/></svg></span>(402) 555-0183</div>
      <div class="phone-line"><span class="phone-icon"><svg viewBox="0 0 10 10"><rect x="2" y="3" width="6" height="5" fill="#fff"/><rect x="3" y="1" width="4" height="2" fill="#fff"/></svg></span>(402) 555-0129</div>
    </div>
    <div class="contact-col">
      <div>5727 E. Larkspur Avenue</div>
      <div>Suite 418</div>
      <div>Omaha, NE 68297</div>
    </div>
    <div class="contact-col">
      <div>dennis@tallowbrookgroup.example</div>
      <div>www.<span class="web-accent">tallowbrookgroup</span>.example</div>
    </div>
  </div>

  <p class="disclosure">Advisory services offered through Marlowe Ridge Advisors, LLC.</p>

  <div class="person">
    <div class="person-name">DENNIS K. HOLLOWAY, MBA</div>
    <div class="person-title">Founder/President</div>
  </div>
</section>

<section class="card card--back" aria-label="Card back">
  <svg class="card-art" viewBox="0 0 540 310" preserveAspectRatio="none" aria-hidden="true">
    <defs>
      <linearGradient id="leafBack" x1="0" y1="0" x2="1" y2="1">
        <stop offset="0" stop-color="#abd036"/>
        <stop offset="1" stop-color="#8fbf34"/>
      </linearGradient>
    </defs>
    <path d="M0,0 L540,0 L540,22 C360,32 170,60 0,112 Z" fill="url(#leafBack)"/>
    <path d="M0,122 C170,72 360,42 540,32 C350,56 170,96 20,150 Z" fill="#1b1b1b"/>
    <path d="M540,310 L0,310 L0,288 C180,278 370,250 540,198 Z" fill="url(#leafBack)"/>
    <path d="M540,188 C370,238 180,268 0,278 C190,254 370,214 520,160 Z" fill="#1b1b1b"/>
  </svg>

  <div class="brand">
    <span class="brand-dot"></span>
    <span class="brand-name">Tallowbrook Partners</span>
  </div>
</section>

</body>
</html>
```